Independence Day Graphics for Sale

I want to create 10 social media graphics (new Pictora size 4:5 (1080 x 1350 pixels) focusing on our July 4th Sale Graphics, using any of the pics attached. Use the attached pics, NO RANDOM STOCK PHOTOGRAPHY. For the color scheme of the graphics, they should all be complementary to the product colors in the photos.
You can add any of the photos attached but none are required. You can do some of the graphics in all text. I mainly need BOLD text that says one of the headlines (10 total) SEE ATTACHED WORD DOCUMENT for the headlines to use.

Target Market(s)

women looking to lose weight

Requirements
Must have
• pics attached and text attached

```html
<!DOCTYPE html>
<html lang="en">
<head>
<meta charset="utf-8">
<title>July 4th Sale Social Graphics</title>
<link rel="stylesheet" href="https://fonts.googleapis.com/css2?family=Bungee&family=Exo+2:wght@500&family=Montserrat:wght@700&family=Playfair+Display:wght@700&family=Rubik:wght@600;700&family=Russo+One&display=swap">
<style>
  :root {
    --page: #ffffff;
    --lilac: #d084db;
    --periwinkle: #6b7ef0;
    --wave-blue: #5f7ff5;
    --forest: #3b5a51;
    --red: #e0453a;
    --plum: #473a6c;
    --rose: #c978a6;
    --ink: #111111;
    --white: #ffffff;
    --photo-top: #6b4534;
    --photo-mid: #a9836b;
    --photo-low: #e9e6e3;
  }
  * { box-sizing: border-box; margin: 0; padding: 0; }
  html, body { width: 1200px; height: 990px; overflow: hidden; background: var(--page); }
  .sheet { position: relative; width: 1200px; height: 990px; }
  .post { position: absolute; width: 336px; height: 420px; overflow: hidden; box-shadow: 0 0 2px rgba(0,0,0,.25); }
  .post svg.art { position: absolute; inset: 0; width: 100%; height: 100%; }
  .row-1 { top: 60px; } .row-2 { top: 510px; }
  .col-1 { left: 50px; } .col-2 { left: 431px; } .col-3 { left: 812px; }

  .seal { position: absolute; display: flex; flex-direction: column; align-items: center; justify-content: center; }
  .seal svg { position: absolute; inset: 0; width: 100%; height: 100%; }
  .seal span { position: relative; line-height: .95; }

  /* Mega sale */
  .mega { background: linear-gradient(180deg, var(--lilac), var(--periwinkle)); }
  .mega .copy { position: absolute; left: 17px; top: 50px; font-family: "Rubik", sans-serif; font-weight: 700; color: var(--white); font-size: 27px; line-height: 34px; }
  .mega .date { display: flex; align-items: center; gap: 5px; margin-bottom: 14px; }
  .mega .date svg { width: 23px; height: 23px; }
  .mega .seal { left: 20px; top: 259px; width: 100px; height: 100px; font-family: "Russo One", sans-serif; color: var(--periwinkle); }
  .mega .seal .big { font-size: 28px; } .mega .seal .small { font-size: 17px; }

  /* Biggest sale */
  .biggest { background: var(--white); }
  .biggest .copy { position: absolute; left: 187px; top: 36px; font-family: "Rubik", sans-serif; font-weight: 700; font-size: 26px; line-height: 37px; color: var(--forest); }
  .biggest .hot { color: var(--red); }
  .biggest .seal { left: 134px; top: 246px; width: 60px; height: 60px; font-family: "Russo One", sans-serif; color: var(--white); }
  .biggest .seal .big { font-size: 17px; } .biggest .seal .small { font-size: 10px; }

  /* Historic */
  .historic { background: var(--forest); }
  .historic .copy { position: absolute; left: 24px; top: 293px; font-family: "Montserrat", sans-serif; font-weight: 700; font-size: 27px; line-height: 37px; color: var(--white); }
  .historic .hot { color: var(--red); }

  /* Stock-up */
  .stockup { background: linear-gradient(180deg, var(--plum), var(--rose)); }
  .stockup .frame { position: absolute; inset: 10px; border: 1.5px solid #1c1626; border-top-color: #e8e2ee; }
  .stockup .seal { left: 118px; top: 40px; width: 100px; height: 100px; font-family: "Russo One", sans-serif; color: var(--plum); font-size: 38px; }
  .stockup .copy { position: absolute; left: 0; right: 0; top: 180px; text-align: center; font-family: "Playfair Display", serif; font-weight: 700; font-size: 30px; line-height: 49px; color: var(--white); }

  /* Biggest discount */
  .discount { background: linear-gradient(180deg, #ffffff, var(--rose)); }
  .discount .frame { position: absolute; inset: 10px; border: 1.5px solid var(--red); border-top-color: var(--forest); }
  .discount .seal { left: 203px; top: 61px; width: 76px; height: 76px; font-family: "Russo One", sans-serif; color: var(--forest); font-size: 28px; }
  .discount .copy { position: absolute; left: 31px; top: 150px; font-family: "Playfair Display", serif; font-weight: 700; font-size: 35px; line-height: 50px; color: var(--ink); }
  .discount .hot { color: var(--red); }

  /* Last chance */
  .lastchance { background: var(--forest); }
  .lastchance .seal { left: 22px; top: 28px; width: 80px; height: 80px; font-family: "Bungee", sans-serif; color: var(--forest); font-size: 12px; text-align: center; }
  .lastchance .copy { position: absolute; left: 0; right: 0; top: 126px; text-align: center; font-family: "Exo 2", sans-serif; font-weight: 500; font-size: 37px; line-height: 50px; color: var(--white); }
</style>
</head>
<body>
<svg width="0" height="0" style="position:absolute" aria-hidden="true">
  <defs>
    <symbol id="seal-shape" viewBox="-50 -50 100 100">
      <rect x="-37" y="-37" width="74" height="74" rx="16"/>
      <rect x="-37" y="-37" width="74" height="74" rx="16" transform="rotate(30)"/>
      <rect x="-37" y="-37" width="74" height="74" rx="16" transform="rotate(60)"/>
    </symbol>
    <linearGradient id="photo-tone" x1="0" y1="0" x2="0" y2="1">
      <stop offset="0" stop-color="#6b4534"/>
      <stop offset=".55" stop-color="#a9836b"/>
      <stop offset=".72" stop-color="#e9e6e3"/>
      <stop offset="1" stop-color="#f2f0ee"/>
    </linearGradient>
  </defs>
</svg>

<main class="sheet">

  <section class="post mega row-1 col-1">
    <svg class="art" viewBox="0 0 336 420">
      <path role="img" aria-label="Photo: smiling woman in a white cropped sweater holding a supplement bottle in a kitchen" d="M160 0 C185 40 188 100 175 150 C160 205 125 240 131 310 C134 350 145 390 157 420 L336 420 L336 0 Z" fill="url(#photo-tone)"/>
      <path d="M160 0 C185 40 188 100 175 150 C160 205 125 240 131 310 C134 350 145 390 157 420" fill="none" stroke="var(--wave-blue)" stroke-width="5"/>
    </svg>
    <div class="copy">
      <div class="date">
        <svg viewBox="0 0 24 24"><rect x="2" y="4" width="20" height="18" rx="3" fill="#fff"/><rect x="6" y="1.5" width="2.5" height="5" rx="1" fill="#fff"/><rect x="15.5" y="1.5" width="2.5" height="5" rx="1" fill="#fff"/><rect x="4.5" y="10" width="15" height="9.5" rx="1.5" fill="#c98bdc"/></svg>
        July 4th
      </div>
      Mega Sale!<br>25% OFF<br>Everything
    </div>
    <div class="seal"><svg fill="#fff"><use href="#seal-shape"/></svg><span class="big">25%</span><span class="small">OFF</span></div>
  </section>

  <section class="post biggest row-1 col-2">
    <svg class="art" viewBox="0 0 336 420">
      <path role="img" aria-label="Photo: smiling woman presenting supplement bottles on a marble counter, with a close-up of bottles below" d="M0 0 L79 0 C145 20 170 70 170 135 L170 286 L200 287 C285 283 330 340 336 420 L0 420 Z" fill="url(#photo-tone)"/>
      <path d="M79 0 C145 20 170 70 170 135 L170 286" fill="none" stroke="var(--red)" stroke-width="3"/>
      <path d="M200 287 C285 283 330 340 336 420" fill="none" stroke="var(--red)" stroke-width="3"/>
    </svg>
    <div class="copy">Biggest<br>4th of July<br><span class="hot">Sale Ever!<br>25% OFF<br>Sitewide</span></div>
    <div class="seal"><svg fill="var(--forest)"><use href="#seal-shape"/></svg><span class="big">25%</span><span class="small">OFF</span></div>
  </section>

  <section class="post historic row-1 col-3">
    <svg class="art" viewBox="0 0 336 420">
      <circle role="img" aria-label="Photo: smiling woman behind a row of supplement bottles in a kitchen" cx="192" cy="134" r="147" fill="url(#photo-tone)" stroke="var(--red)" stroke-width="3"/>
    </svg>
    <div class="copy">Historic <span class="hot">4th</span> of July<br>Sale!&nbsp; <span class="hot">25%</span> OFF of<br>Everything</div>
  </section>

  <section class="post stockup row-2 col-1">
    <div class="frame"></div>
    <div class="seal"><svg fill="#fff"><use href="#seal-shape"/></svg><span>25%</span></div>
    <div class="copy">25% OFF Stock-Up<br>Event:&nbsp; 25% OFF<br>All Supplements</div>
  </section>

  <section class="post discount row-2 col-2">
    <div class="frame"></div>
    <svg class="art" viewBox="0 0 336 420">
      <polygon points="267,10 326,10 326,62 262,132 205,78" fill="var(--forest)"/>
      <circle cx="241" cy="99" r="48" fill="var(--forest)"/>
    </svg>
    <div class="seal"><svg fill="#fff"><use href="#seal-shape"/></svg><span>25%</span></div>
    <div class="copy">Our Biggest<br>Discount Ever!<br><span class="hot">25%</span> OFF<br>Everything</div>
  </section>

  <section class="post lastchance row-2 col-3">
    <svg class="art" viewBox="0 0 336 420">
      <defs><clipPath id="inner-frame"><rect x="9" y="9" width="318" height="402"/></clipPath></defs>
      <g clip-path="url(#inner-frame)" fill="var(--red)">
        <circle cx="318" cy="30" r="76"/>
        <circle cx="33" cy="402" r="68"/>
      </g>
      <rect x="9" y="9" width="318" height="402" fill="none" stroke="#fff" stroke-width="1.5"/>
    </svg>
    <div class="seal"><svg fill="#fff"><use href="#seal-shape"/></svg><span>Special<br>Offer</span></div>
    <div class="copy">Last Chance<br>25% OFF<br>Time Is<br>Running Out!</div>
  </section>

</main>
</body>
</html>
```